Graphic Design/Logo Needed for Ear Drops Bottle

We have an Ear Drop Medication that we need to create a new label for. We will use a retro picture of a Doctor (Dr. Halvane) and the name of the product is Mighty Lobe. There is no official logo, so we will want to create a retro, basic logo for Mighty Lobe and use the retro picture. Front portion of the label is Size is 1.5" in height, and about 1.375" Width. this is a small tube similar in size to eye drops. We will be looking for just the logo portion and what you will see on the front of the bottle.

Target Market(s)

Medical Container

Industry/Entity Type

Medical

Font styles to use
Serif
Sans Serif

Colors
0054AA
0677BA
7BADD7
CADEEF
E8F1F8
FFF300
FFF600
FEFA6F
FFFEC7
FFFEE8

Requirements
Must have
• Picture of Dr. Halvane, "Mighty Lobe", Dr. Halvane's Ear Solution
Nice to have
• Retro Style or Modern with Retro Feel, Clean and engaging

```html
<!DOCTYPE html>
<html lang="en">
<head>
<meta charset="utf-8">
<title>Mighty Lobe — Label Variants</title>
<link rel="stylesheet" href="https://fonts.googleapis.com/css2?family=Oswald:wght@400;700&display=swap">
<style>
  :root {
    --page: #ffffff;
    --teal-bg: #5b949c;
    --teal-band: #1f5b5d;
    --teal-line: #e9f3f3;
    --teal-photo-a: #c9cfcf;
    --teal-photo-b: #8f9a9a;
    --tan-bg: #c6bdab;
    --tan-band: #333333;
    --tan-line: #f4f0e8;
    --tan-photo-a: #c9c2b2;
    --tan-photo-b: #8d877a;
    --ice-bg: #e4e9ea;
    --ice-band: #2a2e3a;
    --ice-line: #2a2e3a;
    --ice-photo-a: #dcdfe0;
    --ice-photo-b: #9a9ea1;
    --ink-light: #f4f4f2;
  }
  html, body {
    margin: 0;
    width: 1200px;
    height: 927px;
    overflow: hidden;
    background: var(--page);
  }
  .label-row {
    position: relative;
    width: 1200px;
    height: 927px;
  }
  .label {
    position: absolute;
    top: 438px;
    width: 290px;
    height: 318px;
  }
  .label--teal { left: 81px; }
  .label--tan  { left: 456px; }
  .label--ice  { left: 821px; }
  .label svg { display: block; width: 100%; height: 100%; }
  .product-name {
    font-family: "Oswald", sans-serif;
    font-weight: 700;
    font-size: 50px;
    fill: var(--ink-light);
  }
  .product-sub {
    font-family: "Oswald", sans-serif;
    font-weight: 400;
    font-size: 23px;
    fill: var(--ink-light);
  }
  .frame-line { fill: none; stroke-width: 1.6; }
  .label--teal .frame-line { stroke: var(--teal-line); }
  .label--tan  .frame-line { stroke: var(--tan-line); }
  .label--ice  .frame-line { stroke: var(--ice-line); }
</style>
</head>
<body>
<main class="label-row">

  <!-- Teal variant -->
  <section class="label label--teal">
    <svg viewBox="0 0 290 318" xmlns="http://www.w3.org/2000/svg">
      <defs>
        <linearGradient id="photo-teal" x1="0" y1="0" x2="0" y2="1">
          <stop offset="0" stop-color="var(--teal-photo-b)"/>
          <stop offset="1" stop-color="var(--teal-photo-a)"/>
        </linearGradient>
      </defs>
      <rect class="label-bg" width="290" height="318" fill="var(--teal-bg)"/>
      <rect class="frame-line" x="9" y="10" width="272" height="300"/>
      <path class="frame-line" d="M9 94 H64 M226 94 H281 M18 94 V226 M272 94 V226 M9 208 H281"/>
      <path class="frame-line" d="M64 208 V101 A81 81 0 0 1 226 101 V208"/>
      <path role="img" aria-label="Retro black-and-white portrait of Dr. Halvane in a white coat and head mirror"
            d="M72 206 V101 A73 73 0 0 1 218 101 V206 Z" fill="url(#photo-teal)"/>
      <rect class="title-band" x="9" y="226" width="272" height="85" fill="var(--teal-band)"/>
      <text class="product-name" x="145" y="275" text-anchor="middle" textLength="222" lengthAdjust="spacingAndGlyphs">MIGHTY LOBE</text>
      <text class="product-sub" x="145" y="303" text-anchor="middle" textLength="230" lengthAdjust="spacingAndGlyphs">DR. HALVANE'S EAR SOLUTION</text>
    </svg>
  </section>

  <!-- Tan variant -->
  <section class="label label--tan">
    <svg viewBox="0 0 290 318" xmlns="http://www.w3.org/2000/svg">
      <defs>
        <linearGradient id="photo-tan" x1="0" y1="0" x2="0" y2="1">
          <stop offset="0" stop-color="var(--tan-photo-b)"/>
          <stop offset="1" stop-color="var(--tan-photo-a)"/>
        </linearGradient>
      </defs>
      <rect class="label-bg" width="290" height="318" fill="var(--tan-bg)"/>
      <rect class="frame-line" x="9" y="10" width="272" height="300"/>
      <path class="frame-line" d="M9 94 H64 M226 94 H281 M18 94 V226 M272 94 V226 M9 208 H281"/>
      <path class="frame-line" d="M64 208 V101 A81 81 0 0 1 226 101 V208"/>
      <path role="img" aria-label="Retro sepia portrait of Dr. Halvane in a white coat and head mirror"
            d="M72 206 V101 A73 73 0 0 1 218 101 V206 Z" fill="url(#photo-tan)"/>
      <rect class="title-band" x="9" y="226" width="272" height="85" fill="var(--tan-band)"/>
      <text class="product-name" x="145" y="275" text-anchor="middle" textLength="222" lengthAdjust="spacingAndGlyphs">MIGHTY LOBE</text>
      <text class="product-sub" x="145" y="303" text-anchor="middle" textLength="230" lengthAdjust="spacingAndGlyphs">DR. HALVANE'S EAR SOLUTION</text>
    </svg>
  </section>

  <!-- Light variant -->
  <section class="label label--ice">
    <svg viewBox="0 0 290 318" xmlns="http://www.w3.org/2000/svg">
      <defs>
        <linearGradient id="photo-ice" x1="0" y1="0" x2="0" y2="1">
          <stop offset="0" stop-color="var(--ice-photo-b)"/>
          <stop offset="1" stop-color="var(--ice-photo-a)"/>
        </linearGradient>
      </defs>
      <rect class="label-bg" width="290" height="318" fill="var(--ice-bg)"/>
      <rect class="frame-line" x="9" y="10" width="272" height="300"/>
      <path class="frame-line" d="M9 94 H64 M226 94 H281 M18 94 V226 M272 94 V226 M9 208 H281"/>
      <path class="frame-line" d="M64 208 V101 A81 81 0 0 1 226 101 V208"/>
      <path role="img" aria-label="Retro grayscale portrait of Dr. Halvane in a white coat and head mirror"
            d="M72 206 V101 A73 73 0 0 1 218 101 V206 Z" fill="url(#photo-ice)"/>
      <rect class="title-band" x="9" y="226" width="272" height="85" fill="var(--ice-band)"/>
      <text class="product-name" x="145" y="275" text-anchor="middle" textLength="222" lengthAdjust="spacingAndGlyphs">MIGHTY LOBE</text>
      <text class="product-sub" x="145" y="303" text-anchor="middle" textLength="230" lengthAdjust="spacingAndGlyphs">DR. HALVANE'S EAR SOLUTION</text>
    </svg>
  </section>

</main>
</body>
</html>
```